Visitenkarten-Design für Ferienhausvermietung
Zielgruppe
Vermietung eines Ferienhauses
Aufgabenstellung
Die Visitenkarte sollte edel und hochwertig wirken...
Es wäre mir wichtig, dass die Visitenkarte im Querformat erstellt wird.
Die Farben vom Logo lauten:
green: C = 43 M = 0 Y = 100 N = 16
brown: C = 39 M = 57 J = 87 N = 53
sky blue: C = 14 M = 6 J = 6 N = 0
Aber bitte nicht so viel in den Visitenkarten verwenden. Die Visitenkarten sollen eher neutral gehalten werden.
Die Schriften
font
Lindeneck : Satisfaction
Ferienhaus : Corbert Regular
Flyer-Design für Ferienhausvermietung Flyer-Design für Ferienhausvermietung"
Es soll ein Flyer im Format DIN A4 erstellt werden. Der beidseitig bedruckt wird und dann 6seitig gefaltet wird. Ich benötige für den Flyer: Beschreibung/Ausstattung des Ferienhauses Beschreibung der Lage Beschreibung der Umgebung Anfahrt/Lage/Kontakt
Logo-Design für Ferienhaus ´Sa Morta´auf Mallorca mit eigenem Tennisplatz und Pool Logo-Design für Ferienhaus ´Sa Morta´auf Mallorca mit eigenem Tennisplatz und Pool"
Sie können sich meine Finca auf der Website: Casitorvent anschauen. Ort: Costitx Name des Hauses: Finca Reblat (heißt nur auf der Website so). Der Name am Tor Haus: Finca Sa Morta. Ich mag es gerne klassisch
Logo-Design für ein Feriendorf an der Ostsee Logo-Design für ein Feriendorf an der Ostsee"
* Nicht zu bunt, nicht zu verspielt, möglichst klar und aufgeräumt * In 2D, keine Schattierungen, keine Fotos im Hintergrund o. ä.. * Das Logo muss in allen Medien gut darstellbar sein! * Es sollte modern wirken, dennoch fröhlich, warm und einladend * Der Strand-/Wasserbezug muss deutlich we..
Flyer-Design für Ferienhaus Flyer-Design für Ferienhaus"
Flyerdesign für Ferienhaus: Din-Lang 2x gefalzt (übliche Format), 3 Seiten vorne und hinten.  Es sollte nach Möglichkeit an unsere Webseite (www.ferienhaus-kormoran-tidewik.de) angepasst werden, druckfertig sein und per PDF auf unserer Webseite zum Downloaden integriert werden können. Meh..
Logo-Design für Ferienhaus Logo-Design für Ferienhaus"
Wir suchen ein Moderenes Design gern berücksichtig in Kombination mit dem Naturpark Velmtaler Höhen. Da das Ferienhaus sich dort befindet.

```html
<!DOCTYPE html>
<html lang="de">
<head>
<meta charset="utf-8">
<title>Ferienhaus Lindeneck – Visitenkarte</title>
<link href="https://fonts.googleapis.com/css2?family=Raleway:wght@400&display=swap" rel="stylesheet">
<style>
  :root {
    --page: #ffffff;
    --brown: #684a20;
    --green: #8cc11f;
    --paper: #e2e6eb;
    --text: #4a3a22;
  }
  html, body {
    margin: 0;
    padding: 0;
    width: 856px;
    height: 1200px;
    overflow: hidden;
    background: var(--page);
    font-family: "Raleway", sans-serif;
  }
  .canvas {
    position: relative;
    width: 856px;
    height: 1200px;
  }
  .card {
    position: absolute;
    left: 148px;
    width: 560px;
    height: 280px;
    box-shadow: 0 10px 24px rgba(0, 0, 0, 0.28);
    overflow: hidden;
  }
  .card--front {
    top: 250px;
    background: var(--brown);
  }
  .card--back {
    top: 640px;
    background: var(--paper);
  }
  .seal {
    position: absolute;
    left: 171px;
    top: 31px;
    width: 218px;
    height: 218px;
    border-radius: 50%;
    background: var(--paper);
    display: flex;
    align-items: center;
    justify-content: center;
  }
  .seal__ring {
    position: absolute;
    left: 46px;
    top: 46px;
    width: 122px;
    height: 122px;
    border: 2px solid var(--brown);
    border-radius: 50%;
    box-sizing: border-box;
  }
  .seal__name {
    position: relative;
    color: var(--brown);
    font-size: 24px;
    letter-spacing: 0.5px;
    background: var(--paper);
    padding: 2px 4px;
  }
  .contact {
    position: absolute;
    left: 25px;
    top: 16px;
    font-size: 14.5px;
    line-height: 17.5px;
    color: var(--text);
  }
  .contact p {
    margin: 0 0 17px 0;
  }
  .contact .accent {
    color: var(--green);
  }
  .house-art {
    position: absolute;
    left: 298px;
    top: 128px;
    width: 244px;
    height: 136px;
  }
</style>
</head>
<body>
<main class="canvas">
  <section class="card card--front" aria-label="Vorderseite">
    <div class="seal">
      <span class="seal__ring" aria-hidden="true"></span>
      <span class="seal__name">Lindeneck</span>
    </div>
  </section>

  <section class="card card--back" aria-label="Rückseite">
    <div class="contact">
      <p>Ferienhaus Lindeneck</p>
      <p class="accent">Tel: 07342 / 58 16 204<br>www.lindeneck-ferienhaus.de</p>
      <p>Birkenweg 7<br>72581 Talbrunn<br>info@lindeneck-ferienhaus.de</p>
    </div>
    <svg class="house-art" viewBox="0 0 244 136" role="img" aria-label="Gezeichnete Ansicht des Ferienhauses mit Bäumen und Wiese">
      <defs>
        <linearGradient id="houseTone" x1="0" y1="0" x2="1" y2="1">
          <stop offset="0" stop-color="#b9cf86"/>
          <stop offset="0.5" stop-color="#a08a66"/>
          <stop offset="1" stop-color="#b9cf86"/>
        </linearGradient>
      </defs>
      <rect x="0" y="0" width="244" height="136" rx="6" fill="url(#houseTone)" opacity="0.55"/>
    </svg>
  </section>
</main>
</body>
</html>
```